Coffee Pouch Label for Coffee Roaster

We are wanting some new labels for our coffee pouches.
We are an established, small family owned specialty coffee roaster called Tarn4 Coffee Roasters, and we are located in Brellin, VIC Australia.
Label dimensions are 100 x 150mm, to fit on a couple of different bag sizes. We use coffee pouches with kraft paper finish.
We have 3 main blends, Lanternfly, Quillrock & Pale Finch, and a range of rotating single origin coffees. We would get labels printed for the blends, but then need a 'generic' design that we can either write the name on, or stick another sticker over for the single origin coffees.
Some information that needs to be on the label:
our logo
web address: www.tarn4coffee.example
address: 47 Corvell St, Brellin, VIC
Proudly Roasted in Brellin, VIC
Blend name
our tagline/mission: roast kindly | share freely | live simply
statement: we give $1 from every kg of coffee sold to local programs that feed, teach and shelter children in need.
We would like to use colour to help differentiate the different blends somehow.
We are after a creative, clean design, that is representative of specialty coffee (not large commercial coffee brands).
I have uploaded our logo both with and without our tagline, and also some other packaging inspiration that i like (I quite like the meadow coffee label design).
thanks everyone!
Marcus
People who appreciate good, local coffee

```html
<!DOCTYPE html>
<html lang="en">
<head>
<meta charset="utf-8">
<title>Tarn4 Coffee Roasters – Blend Labels</title>
<link href="https://fonts.googleapis.com/css2?family=Lexend:wght@400;500;700&display=swap" rel="stylesheet">
<style>
  :root {
    --page: #ffffff;
    --pattern-light: #f1f1f1;
    --pattern-mid: #dcdcdc;
    --ink: #2a2a2a;
    --lanternfly: #b8b8b8;
    --pale-finch: #3b3b3b;
    --pale-finch-ink: #b5b5b5;
    --quillrock: #e2a27f;
  }
  * { margin: 0; padding: 0; box-sizing: border-box; }
  html, body { width: 1200px; height: 759px; overflow: hidden; background: var(--page); }
  body { font-family: "Lexend", sans-serif; color: var(--ink); }

  .label-row {
    position: absolute; left: 70px; top: 140px;
    display: flex; gap: 50px;
  }
  .label {
    position: relative; width: 320px; height: 480px; overflow: hidden;
    background: var(--pattern-light);
  }
  .bean-pattern {
    position: absolute; left: 0; top: 0; width: 100%; height: 220px;
    background:
      radial-gradient(circle at 30% 40%, var(--pattern-light), transparent 60%),
      linear-gradient(180deg, var(--pattern-light), var(--pattern-mid));
  }
  .brand {
    position: absolute; right: 26px; top: 36px; text-align: right;
    font-weight: 700; color: var(--ink);
  }
  .brand-name { display: block; font-size: 28px; line-height: 1; letter-spacing: -0.5px; }
  .brand-sub { display: block; font-size: 6px; letter-spacing: 1px; text-transform: uppercase; margin-top: 3px; }

  .blend-panel { position: absolute; left: 0; right: 0; top: 200px; bottom: 0; }
  .scallops { position: absolute; left: 0; top: 0; width: 320px; height: 24px; }

  .lanternfly .blend-panel { background: var(--lanternfly); }
  .pale-finch .blend-panel { background: var(--pale-finch); color: var(--pale-finch-ink); }
  .quillrock .blend-panel { background: var(--quillrock); }

  .blend-name {
    position: absolute; left: 18px; top: 34px;
    font-size: 36px; font-weight: 700; letter-spacing: -0.3px; line-height: 1;
  }
  .tagline { position: absolute; left: 20px; top: 72px; font-size: 10px; white-space: nowrap; }
  .category {
    position: absolute; left: 20px; top: 136px;
    font-size: 14px; line-height: 1.15; text-transform: uppercase;
  }
  .details { position: absolute; left: 20px; top: 188px; font-size: 9px; line-height: 1.3; }
  .details .web { font-size: 10px; margin-bottom: 2px; }
  .statement { position: absolute; left: 20px; top: 234px; width: 210px; font-size: 6px; line-height: 1.3; }
  .weight { position: absolute; right: 26px; top: 238px; font-size: 13px; font-weight: 700; }
</style>
</head>
<body>
  <main class="label-row">

    <article class="label lanternfly">
      <div class="bean-pattern" role="img" aria-label="Line pattern of overlapping coffee beans"></div>
      <div class="brand"><span class="brand-name">Tarn4</span><span class="brand-sub">Coffee Roasters</span></div>
      <section class="blend-panel">
        <h2 class="blend-name">Lanternfly</h2>
        <p class="tagline">roast kindly | share freely | live simply</p>
        <p class="category">Single Origin<br>Coffee</p>
        <div class="details">
          <p class="web">www.tarn4coffee.example</p>
          <p>proudly roasted in Brellin, VIC</p>
          <p>47 Corvell St, Brellin, VIC</p>
        </div>
        <p class="statement">we give $1 from every kg of coffee sold to local programs that feed, teach and shelter children in need.</p>
        <p class="weight">300g</p>
      </section>
    </article>

    <article class="label pale-finch">
      <div class="bean-pattern" role="img" aria-label="Line pattern of overlapping coffee beans"></div>
      <div class="brand"><span class="brand-name">Tarn4</span><span class="brand-sub">Coffee Roasters</span></div>
      <section class="blend-panel">
        <svg class="scallops" viewBox="0 0 320 24" aria-hidden="true">
          <g fill="#dcdcdc">
            <circle cx="0" cy="0" r="22"/><circle cx="40" cy="0" r="22"/><circle cx="80" cy="0" r="22"/>
            <circle cx="120" cy="0" r="22"/><circle cx="160" cy="0" r="22"/><circle cx="200" cy="0" r="22"/>
            <circle cx="240" cy="0" r="22"/><circle cx="280" cy="0" r="22"/><circle cx="320" cy="0" r="22"/>
          </g>
        </svg>
        <h2 class="blend-name">Pale Finch</h2>
        <p class="tagline">roast kindly | share freely | live simply</p>
        <p class="category">Single Origin<br>Coffee</p>
        <div class="details">
          <p class="web">www.tarn4coffee.example</p>
          <p>proudly roasted in Brellin, VIC</p>
          <p>47 Corvell St, Brellin, VIC</p>
        </div>
        <p class="statement">we give $1 from every kg of coffee sold to local programs that feed, teach and shelter children in need.</p>
        <p class="weight">300g</p>
      </section>
    </article>

    <article class="label quillrock">
      <div class="bean-pattern" role="img" aria-label="Line pattern of overlapping coffee beans"></div>
      <div class="brand"><span class="brand-name">Tarn4</span><span class="brand-sub">Coffee Roasters</span></div>
      <section class="blend-panel">
        <svg class="scallops" viewBox="0 0 320 24" aria-hidden="true">
          <g fill="#dcdcdc">
            <circle cx="0" cy="0" r="22"/><circle cx="40" cy="0" r="22"/><circle cx="80" cy="0" r="22"/>
            <circle cx="120" cy="0" r="22"/><circle cx="160" cy="0" r="22"/><circle cx="200" cy="0" r="22"/>
            <circle cx="240" cy="0" r="22"/><circle cx="280" cy="0" r="22"/><circle cx="320" cy="0" r="22"/>
          </g>
        </svg>
        <h2 class="blend-name">Quillrock</h2>
        <p class="tagline">roast kindly | share freely | live simply</p>
        <p class="category">Single Origin<br>Coffee</p>
        <div class="details">
          <p class="web">www.tarn4coffee.example</p>
          <p>proudly roasted in Brellin, VIC</p>
          <p>47 Corvell St, Brellin, VIC</p>
        </div>
        <p class="statement">we give $1 from every kg of coffee sold to local programs that feed, teach and shelter children in need.</p>
        <p class="weight">300g</p>
      </section>
    </article>

  </main>
</body>
</html>
```